Professional & Modern Technology Business Card

We need a business card for our software/technology firm. Our services include Program/Project Management, Project Controls and Enterprise Analytics. Our clients are usually in the Aviation, Public Works, Transportation and Electric & Water Utility industries. We serve both public and private clients. Would like a very professional, conservative but somewhat modern design. Design, Develop, Deploy is the corporate tagline. We have two offices. The headquarters is in Atlanta, GA and a satellite office In Savannah, GA. Corporate Logo Attached.
Looking to do website and corporate brochure after the successful completion of this project. Would like to begin a working relationship with best designers.
Tagline: Design, Develop, Deploy
Website: www.quelvanesystems.example
My Name: Marla Dunstead
My Title: CEO
Email: mdunstead@quelvanesystems.example
Atlanta Address:
87 Corliss Avenue, #2291
Atlanta, GA 30301
Office: 404.555.0182
Fax: 404.555.0147
Mobile: 404.555.0163
Savannah Address:
350 West Harrow Bend Road
Suite 720
Savannah, GA 31401
Office: 912.555.0139
Fax: 404.555.0147
Mobile: 404.555.0163
Updates
Please include the email address in your designs: mdunstead@quelvanesystems.example.
I appreciate everyone's design efforts. Just a few notes:
1. Please remove the mobile number from the cards
2. The backs of the cards can be utilized for writing notes. Make sure your design on the back of the card is conducive to clearly adding writing if needed.
3. No black backgrounds please
4. Only use the corporate logo on the front of the card. You can use portions of the logo design, but not the logo in totality.
Thank You
Industry/Entity Type
Conservative
Look and feel
Each slider illustrates characteristics of the customer's brand and the style your logo design should communicate.

```html
<!DOCTYPE html>
<html lang="en">
<head>
<meta charset="utf-8">
<title>Marla Dunstead – Business Card</title>
<link rel="stylesheet" href="https://fonts.googleapis.com/css2?family=Arimo:ital,wght@0,400;0,700;1,400;1,700&display=swap">
<style>
  :root {
    --navy: #2a3a82;
    --blue: #1d6fb8;
    --cyan: #22aee0;
    --magenta: #c8226f;
    --plum: #6b1c5a;
    --text: #ffffff;
    --gold: #e8b430;
  }
  html, body {
    margin: 0;
    padding: 0;
    width: 1200px;
    height: 723px;
    overflow: hidden;
    background: #ffffff;
  }
  .card {
    position: relative;
    width: 1200px;
    height: 723px;
    overflow: hidden;
    font-family: "Arimo", Arial, sans-serif;
    color: var(--text);
  }
  .card-bg {
    position: absolute;
    inset: 0;
  }
  .identity {
    position: absolute;
    left: 80px;
    top: 72px;
  }
  .person-name {
    margin: 0;
    font-size: 35px;
    font-weight: 700;
    line-height: 1.1;
  }
  .person-title {
    margin: 6px 0 0;
    font-size: 20px;
    font-style: italic;
  }
  .office {
    position: absolute;
    left: 79px;
    margin: 0;
    font-style: normal;
    font-size: 28px;
    line-height: 37.3px;
  }
  .office--savannah { top: 209px; }
  .office--atlanta { top: 428px; }
  .email {
    position: absolute;
    left: 79px;
    top: 651px;
    font-size: 28px;
  }
  .brand {
    position: absolute;
    left: 760px;
    top: 440px;
    display: flex;
    align-items: center;
    gap: 14px;
  }
  .brand-dot {
    width: 40px;
    height: 40px;
    border-radius: 50%;
    background: var(--gold);
    flex: none;
  }
  .brand-name {
    font-size: 33px;
    font-weight: 700;
    line-height: 1.05;
    color: var(--text);
  }
  .tagline {
    position: absolute;
    right: 82px;
    top: 578px;
    margin: 0;
    font-size: 29px;
    font-style: italic;
    font-weight: 700;
    color: var(--gold);
  }
  .website {
    position: absolute;
    right: 83px;
    top: 651px;
    font-size: 28px;
  }
</style>
</head>
<body>
<div class="card">
  <svg class="card-bg" width="1200" height="723" viewBox="0 0 1200 723" aria-hidden="true">
    <defs>
      <radialGradient id="blueGlow" cx="62%" cy="40%" r="75%">
        <stop offset="0" stop-color="var(--cyan)"/>
        <stop offset="0.45" stop-color="var(--blue)"/>
        <stop offset="1" stop-color="var(--navy)"/>
      </radialGradient>
      <linearGradient id="magentaBand" x1="0.3" y1="0.2" x2="0.9" y2="1">
        <stop offset="0" stop-color="var(--magenta)"/>
        <stop offset="0.55" stop-color="#a01f69"/>
        <stop offset="1" stop-color="var(--plum)"/>
      </linearGradient>
      <linearGradient id="bandEdge" x1="0" y1="0" x2="1" y2="0">
        <stop offset="0" stop-color="#e04590" stop-opacity="0.9"/>
        <stop offset="1" stop-color="#e04590" stop-opacity="0"/>
      </linearGradient>
    </defs>
    <rect width="1200" height="723" fill="url(#blueGlow)"/>
    <polygon points="1200,73 1200,723 413,723" fill="url(#magentaBand)"/>
    <polygon points="1200,73 1200,110 455,723 413,723" fill="url(#bandEdge)" opacity="0.55"/>
  </svg>

  <header class="identity">
    <h1 class="person-name">Marla Dunstead</h1>
    <p class="person-title">CEO</p>
  </header>

  <address class="office office--savannah">
    350 West Harrow Bend Road<br>
    Suite 720, Savannah, GA 31401<br>
    Office: 912.555.0139<br>
    Fax: 404.555.0147<br>
    Mobile: 404.555.0163
  </address>

  <address class="office office--atlanta">
    87 Corliss Avenue, #2291<br>
    Atlanta, GA 30301<br>
    Office: 404.555.0182<br>
    Fax: 404.555.0147<br>
    Mobile: 404.555.0163
  </address>

  <div class="email">mdunstead@quelvanesystems.example</div>

  <div class="brand">
    <span class="brand-dot"></span>
    <span class="brand-name">Quelvane<br>Systems, Inc.</span>
  </div>

  <p class="tagline">Design, Develop, Deploy</p>

  <div class="website">www.quelvanesystems.example</div>
</div>
</body>
</html>
```